Creation of an elegant and modern turnkey Shopify website

Hello,

We are a new company specializing in the sale of above-ground pools. We want to create a turnkey website, ideally using Shopify. For now, we need a "showcase" site, not an e-commerce platform, with four tabs:

Home Page (an overall presentation of the company)
Our Products (an overview of all the above-ground pools we sell)
Our Projects (a page inspired by Instagram to showcase photos of our future projects)
Contact (a page with all our contact information and a contact form)

We are looking to create a highly visual, elegant, and modern website with vibrant splashes of color. We will provide the text, photos (along with instructions on where to place them on each page), and all other necessary information as attachments.

Thank you in advance for your proposals!

The Larkmere Basin Team

Target Market(s)

Targeted at Swiss customers (a translator will need to be installed for different languages)

Industry/Entity Type

Sale of customised above-ground pools

Coding

Coded - Design and coding required

Font styles to use
Sans Serif

Colors
0094D4
00A9DD
6FCCEA
C7EBF8
E9F6FB
00AB8E
00BBA5
67D7C9
C6EFE9
E9F9F6

Requirements
Must have
• A stunning, elegant and modern look
Nice to have
• Inspiration from the colors of our logo throughout the site, but in an elegant way
Should not have
• An overly classic look for swimming pool sites

```html
<!DOCTYPE html>
<html lang="en">
<head>
<meta charset="utf-8">
<title>Larkmere Basin – Above-Ground Pools</title>
<link rel="stylesheet" href="https://fonts.googleapis.com/css2?family=Marcellus&family=Lato:wght@400;700&display=swap">
<style>
:root{
  --blue-deep:#0094D4;
  --blue:#00A9DD;
  --cyan:#1CC6E0;
  --sky:#6FCCEA;
  --teal:#00AB8E;
  --page:#EFFDFE;
  --ink:#4a4a4a;
  --text:#5b5b5b;
  --footer:#1f1f1f;
  --white:#ffffff;
}
*{box-sizing:border-box;margin:0;padding:0}
html,body{width:1200px;height:3163px;overflow:hidden}
body{background:var(--page);font-family:"Lato",sans-serif;color:var(--text);position:relative}
.abs{position:absolute}
.topbar{left:0;top:0;width:1200px;height:32px;background:var(--blue-deep);color:var(--white);font-weight:700;font-size:12px;display:flex;align-items:center;justify-content:center;letter-spacing:-.2px}
.brand{font-family:"Marcellus",serif;color:var(--cyan);line-height:1;letter-spacing:2px;text-transform:uppercase}
.header-brand{left:144px;top:52px;font-size:36px}
.nav{top:85px;font-size:12px;font-weight:700;color:#222;letter-spacing:-.1px}
.nav a{color:inherit;text-decoration:none;position:absolute;white-space:nowrap}
.search{left:1038px;top:84px}
.heading{font-family:"Marcellus",serif;text-transform:uppercase;color:var(--ink);font-weight:400;line-height:47px;font-size:39px}
.heading .hl{color:var(--cyan)}
.body-text{font-size:13.5px;line-height:24.5px;text-align:justify}
.btn{display:flex;align-items:center;justify-content:center;font-weight:700;font-size:16px;letter-spacing:-.3px;text-decoration:none}
.btn-teal{background:var(--teal);color:var(--white)}
.btn-white{background:var(--white);color:var(--blue-deep)}
.photo{display:block}
.acc-item{left:631px;width:425px;background:var(--white);display:flex;align-items:center;padding:0 36px;font-size:23px;color:#222}
.acc-item .chev{position:absolute;right:30px;top:50%;margin-top:-5px}
.acc-open{background:var(--teal);color:var(--white);display:block;padding:20px 28px 0 38px}
.acc-open p{font-size:13.5px;line-height:25px;margin-top:18px}
.cta{left:0;top:2543px;width:1200px;height:250px;background:var(--blue-deep)}
.footer{left:0;top:2793px;width:1200px;height:370px;background:var(--footer);color:var(--white)}
.footer-menu h4{font-family:"Lato",sans-serif;font-weight:400;color:var(--blue);font-size:21px}
.footer-menu a{display:block;color:var(--white);text-decoration:none;font-size:13.5px;line-height:24.5px}
</style>
</head>
<body>

<div class="abs topbar">CHECK OUT OUR LATEST PRODUCTS</div>

<div class="abs brand header-brand">Larkmere<br>Basin</div>

<nav class="abs nav" style="left:0;width:1200px">
  <a href="#" style="left:646px">HOME</a>
  <a href="#" style="left:711px">OUR PRODUCTS</a>
  <a href="#" style="left:830px">OUR PROJECTS</a>
  <a href="#" style="left:943px">CONTACT</a>
</nav>
<svg class="abs search" width="16" height="16" viewBox="0 0 16 16" aria-label="Search"><circle cx="6.5" cy="6.5" r="4.8" fill="none" stroke="#111" stroke-width="2.2"/><line x1="10" y1="10" x2="14.5" y2="14.5" stroke="#111" stroke-width="2.6" stroke-linecap="round"/></svg>

<!-- Hero -->
<h1 class="abs heading" style="left:144px;top:176px;width:420px">Transform your <span class="hl">garden with our</span> premium above-<span class="hl">ground pools!</span></h1>
<p class="abs body-text" style="left:144px;top:375px;width:386px">Achieve your dreams with our custom, tailor-made above-ground pools.Imagine an exceptional relaxation and leisure space right in your own backyard. With our unparalleled expertise and commitment to excellence, we create above-ground pools that exceed all expectations. Our exclusive, custom-designed models are crafted to combine style, durability, and innovation, offering a unique and refined experience.</p>
<a class="abs btn btn-teal" href="#" style="left:144px;top:570px;width:162px;height:51px">GET STARTED</a>
<div class="abs photo" role="img" aria-label="Photo: aerial view of a person relaxing on a float in clear pool water" style="left:551px;top:145px;width:505px;height:518px;background:linear-gradient(135deg,#8fd3d8,#b3e2e4)"></div>

<!-- Personalized services -->
<div class="abs photo" role="img" aria-label="Photo: colourful pool float on bright blue water" style="left:144px;top:737px;width:267px;height:337px;background:linear-gradient(160deg,#3fc6ec,#1aa9d8)"></div>
<div class="abs photo" role="img" aria-label="Photo: resort pool with ladder and palm trees" style="left:413px;top:737px;width:267px;height:337px;background:linear-gradient(180deg,#6fb8cf,#a9d6e0)"></div>
<h2 class="abs heading" style="left:732px;top:790px;width:330px">Personalized <span class="hl">services</span></h2>
<p class="abs body-text" style="left:732px;top:897px;width:307px">We understand that every garden and client is unique. That's why we offer personalized services, from design to installation and after-sales support. Our team of experts is here to answer all your questions and guide you throughout your project.</p>

<!-- Guaranteed satisfaction -->
<h2 class="abs heading" style="left:143px;top:1178px;width:340px">Guaranteed <span class="hl">satisfaction</span></h2>
<p class="abs body-text" style="left:143px;top:1285px;width:305px">Your satisfaction is our top priority. We are committed to providing you with exceptional service and the highest quality products. Join our community of satisfied customers who are already enjoying their custom above-ground pools. 10-Year Warranty!</p>
<div class="abs photo" role="img" aria-label="Photo: person in a sun hat relaxing at the pool edge" style="left:501px;top:1126px;width:268px;height:335px;background:linear-gradient(180deg,#1a9fd6,#3bb8e6)"></div>
<div class="abs photo" role="img" aria-label="Photo: continuation of the pool-edge scene" style="left:771px;top:1126px;width:268px;height:335px;background:linear-gradient(180deg,#2ab0e2,#43c0e7)"></div>

<!-- Why choose -->
<h2 class="abs heading" style="left:144px;top:1545px;width:1000px;font-size:38px;white-space:nowrap">Why choose our <span class="hl">above-ground pools?</span></h2>
<div class="abs photo" role="img" aria-label="Photo: overhead view of a tiled pool with rippling blue water" style="left:0;top:1622px;width:599px;height:448px;background:linear-gradient(135deg,#1d9ad0,#2ab0e2)"></div>

<div class="abs acc-item acc-open" style="top:1622px;height:146px">
  <div style="font-size:23px">1.&nbsp; Superior Quality</div>
  <svg class="chev" style="top:34px;margin-top:0" width="14" height="8" viewBox="0 0 14 8"><polyline points="1,7 7,1 13,7" fill="none" stroke="#fff" stroke-width="1.4"/></svg>
  <p>Each pool is constructed with high-quality materials, ensuring exceptional durability and strength.</p>
</div>
<div class="abs acc-item" style="top:1778px;height:64px">2.&nbsp; Elegant Design<svg class="chev" width="14" height="8" viewBox="0 0 14 8"><polyline points="1,1 7,7 13,1" fill="none" stroke="#333" stroke-width="1.4"/></svg></div>
<div class="abs acc-item" style="top:1853px;height:64px">3.&nbsp; Custom and Tailor-Made<svg class="chev" width="14" height="8" viewBox="0 0 14 8"><polyline points="1,1 7,7 13,1" fill="none" stroke="#333" stroke-width="1.4"/></svg></div>
<div class="abs acc-item" style="top:1928px;height:64px">4.&nbsp; Easy Installation<svg class="chev" width="14" height="8" viewBox="0 0 14 8"><polyline points="1,1 7,7 13,1" fill="none" stroke="#333" stroke-width="1.4"/></svg></div>
<div class="abs acc-item" style="top:2003px;height:65px">5.&nbsp; Constant Innovation<svg class="chev" width="14" height="8" viewBox="0 0 14 8"><polyline points="1,1 7,7 13,1" fill="none" stroke="#333" stroke-width="1.4"/></svg></div>

<!-- Contact us -->
<div class="abs photo" role="img" aria-label="Photo: modern white villa with an infinity pool by the sea" style="left:144px;top:2138px;width:267px;height:335px;background:linear-gradient(180deg,#b9d2ea,#e8e8e5)"></div>
<div class="abs photo" role="img" aria-label="Photo: person in a turquoise sun hat beside shimmering pool water" style="left:413px;top:2138px;width:267px;height:335px;background:linear-gradient(180deg,#bfe6e4,#72c9cb)"></div>
<h2 class="abs heading" style="left:732px;top:2207px;width:330px">Contact us <span class="hl">today</span></h2>
<p class="abs body-text" style="left:732px;top:2304px;width:307px">Don't wait any longer to transform your garden into a wellness oasis. Contact us today to discover our range of customizable above-ground pools and get a tailored quote. Dive into a world of infinite possibilities with Larkmere Basin</p>

<!-- CTA -->
<div class="abs cta">
  <h2 class="abs heading" style="left:0;top:64px;width:1200px;text-align:center;color:var(--white);font-size:38px">We bring your pool dreams to life!</h2>
  <a class="abs btn btn-white" href="#" style="left:519px;top:129px;width:161px;height:50px">GET STARTED</a>
</div>

<!-- Footer -->
<footer class="abs footer">
  <div class="abs footer-menu" style="left:187px;top:60px">
    <h4>MENUS</h4>
    <a href="#">Home</a><a href="#">Our Products</a><a href="#">Our Projects</a><a href="#">Contact</a>
  </div>
  <div class="abs brand" style="left:410px;top:48px;width:180px;text-align:center;font-size:36px">Larkmere<br>Basin</div>
  <p class="abs body-text" style="left:691px;top:60px;width:322px;color:var(--white)">Sed ut perspiciatis unde omnis iste natus error sit voluptatem accusantium doloremque laudantium, totam rem aperiam, eaque ipsa quae ab illo in</p>
  <svg class="abs" style="left:555px;top:209px" width="90" height="26" viewBox="0 0 90 26" aria-label="Social links">
    <circle cx="13" cy="13" r="12" fill="#e9e9e9"/><circle cx="45" cy="13" r="12" fill="#e9e9e9"/><circle cx="77" cy="13" r="12" fill="#e9e9e9"/>
  </svg>
  <svg class="abs" style="left:489px;top:261px" width="222" height="19" viewBox="0 0 222 19" aria-label="Accepted payment methods">
    <rect x="0" y="0" width="28" height="19" rx="2" fill="#f2f2f2"/>
    <rect x="39" y="0" width="28" height="19" rx="2" fill="#f2f2f2"/>
    <rect x="77" y="0" width="28" height="19" rx="2" fill="#f2f2f2"/>
    <rect x="116" y="0" width="28" height="19" rx="2" fill="#f2f2f2"/>
    <rect x="155" y="0" width="28" height="19" rx="2" fill="#f2f2f2"/>
    <rect x="194" y="0" width="28" height="19" rx="2" fill="#f2f2f2"/>
  </svg>
  <div class="abs" style="left:0;top:308px;width:1200px;text-align:center;font-size:13.5px">© 2024,Larkmere Basin.All Rights Reserved &nbsp;|&nbsp; Privacy &nbsp;|&nbsp; Terms of Use</div>
</footer>

</body>
</html>
```